Medical Company in need of Modern business card design for new Wound Care clinic.

Modern business card design for our Woundcare company. Logo and description of services can be found on our website; https://www.tovrel-woundcare.com/

```html
<!DOCTYPE html>
<html lang="en">
<head>
<meta charset="utf-8">
<title>Tovrel Woundcare – Business Card</title>
<link rel="stylesheet" href="https://fonts.googleapis.com/css2?family=Montserrat:wght@400;500;700&display=swap">
<style>
  :root {
    --backdrop: #3b3b3b;
    --card: #222222;
    --card-edge: #1b1b1b;
    --gold: #c8922f;
    --white: #f2f2f2;
    --rule: #d9d9d9;
    --pattern-dark: #1c1c1c;
    --pattern-light: #2b2b2b;
  }
  * { box-sizing: border-box; margin: 0; padding: 0; }
  html, body { width: 1200px; height: 694px; overflow: hidden; }
  body {
    background: var(--backdrop);
    font-family: "Montserrat", sans-serif;
    position: relative;
  }
  .card {
    position: absolute;
    top: 187px;
    width: 560px;
    height: 320px;
    background: var(--card);
    border: 1px solid var(--card-edge);
    overflow: hidden;
  }
  .card--back { left: 27px; }
  .card--front { left: 613px; }

  /* Back side */
  .back-pattern {
    position: absolute;
    inset: 0;
    background: linear-gradient(135deg, var(--pattern-dark) 0%, var(--pattern-light) 55%, var(--pattern-dark) 100%);
  }
  .back-brand {
    position: absolute;
    inset: 0;
    display: flex;
    align-items: center;
    justify-content: center;
    gap: 10px;
    color: var(--gold);
    font-weight: 500;
    font-size: 17px;
    letter-spacing: 5px;
  }
  .brand-mark {
    width: 12px; height: 12px;
    background: var(--gold);
    flex: none;
  }

  /* Front side */
  .front-brand {
    position: absolute;
    top: 70px;
    right: 40px;
    display: flex;
    align-items: center;
    gap: 10px;
    color: var(--gold);
    font-weight: 500;
    font-size: 17px;
    letter-spacing: 5px;
  }
  .person {
    position: absolute;
    left: 40px;
    top: 150px;
  }
  .person__name {
    color: var(--gold);
    font-weight: 700;
    font-size: 24px;
    letter-spacing: 0.5px;
  }
  .person__title {
    color: var(--white);
    font-size: 12.5px;
    font-weight: 400;
    letter-spacing: 0.5px;
    margin-top: 2px;
  }
  .divider {
    position: absolute;
    top: 208px;
    left: 40px;
    right: 40px;
    height: 1px;
    background: var(--rule);
  }
  .contacts {
    position: absolute;
    left: 40px;
    top: 220px;
    list-style: none;
  }
  .contacts li {
    display: flex;
    align-items: center;
    gap: 10px;
    color: var(--white);
    font-size: 13px;
    line-height: 21px;
    white-space: nowrap;
  }
  .contacts svg { width: 14px; height: 14px; flex: none; }
  .address {
    position: absolute;
    right: 40px;
    top: 222px;
    text-align: right;
    color: var(--white);
    font-size: 13px;
    line-height: 21px;
    font-style: normal;
    white-space: nowrap;
  }
</style>
</head>
<body>

  <section class="card card--back">
    <div class="back-pattern" role="img" aria-label="Tone-on-tone embossed repeating brand pattern"></div>
    <div class="back-brand"><span class="brand-mark"></span>TOVREL WOUNDCARE</div>
  </section>

  <section class="card card--front">
    <div class="front-brand"><span class="brand-mark"></span>TOVREL WOUNDCARE</div>

    <div class="person">
      <p class="person__name">MARCUS HALE</p>
      <p class="person__title">MANAGING DIRECTOR</p>
    </div>
    <div class="divider"></div>

    <ul class="contacts">
      <li>
        <svg viewBox="0 0 14 14" fill="none" stroke="var(--gold)" stroke-width="1.4"><rect x="3.5" y="1" width="7" height="12" rx="1.2"/><line x1="6" y1="11" x2="8" y2="11"/></svg>
        044-318 270 615
      </li>
      <li>
        <svg viewBox="0 0 14 14" fill="var(--gold)"><path d="M3 1.5l2.2 2.6-1.2 1.4c.8 1.8 2.1 3.1 3.9 3.9l1.4-1.2 2.6 2.2-1.3 2C6 12 2 8 1.1 2.8z"/></svg>
        044-318 270 942
      </li>
      <li>
        <svg viewBox="0 0 14 14" fill="none" stroke="var(--gold)" stroke-width="1.4"><rect x="1" y="3" width="12" height="8"/><polyline points="1,3 7,8 13,3"/></svg>
        care@tovrel.com
      </li>
      <li>
        <svg viewBox="0 0 14 14" fill="none" stroke="var(--gold)" stroke-width="1.3"><circle cx="7" cy="7" r="6"/><ellipse cx="7" cy="7" rx="2.6" ry="6"/><line x1="1" y1="7" x2="13" y2="7"/></svg>
        www.tovrel-woundcare.com
      </li>
    </ul>

    <address class="address">
      27, Larkspur Medical Court<br>
      60418, Westbrook Vale
    </address>
  </section>

</body>
</html>
```